Steel Company / Iron Railing Business Card Template

We are a custom steel fabrication company located in Alder Falls, OH. In business since 1986, we recently developed a new logo, and we're looking for a business card design to help display the new logo and our business. The name of the company is Kelbrook Forge Co.. The Office Phone number is (440) 555-0143. We fabricate and install custom "wrought iron" railings on our residential side, we also fabricate and erect structural steel (think cranes and steel beams in buildings) on our commercial side. Looking to get a business card template designed. Something modern, but professional. Clear and easy to read. Front should have all business and employee information including phone number(s), email address, business information, etc. back should spotlight logo.

Industry/Entity Type

Construction / Home Improvement

Contact Information for Business Card

Business information is Kelbrook Forge Co., 48 Dunmore Ave Suite 3305, Alder Falls, OH 44074. Phone number is (440) 555-0143. Website is www.kelbrookforge.example Business card should be for "Tom Pelling" with the job title "Sales & Estimating" but be editable for other employees. Tom's phone number is (610) 555-0178

Colors

Designer to choose colors to be used in the design.

Requirements
Must have
• Modern Feel, Design should be sized for standard business card sizing 3.5" x 2" (88.9mm x 50.8mm)

```html
<!DOCTYPE html>
<html lang="en">
<head>
<meta charset="utf-8">
<title>Kelbrook Forge Co. – Business Card</title>
<link rel="stylesheet" href="https://fonts.googleapis.com/css2?family=Ubuntu:wght@400;500;700&display=swap">
<style>
  :root {
    --stage: #e6e7ea;
    --royal: #2b4c9b;
    --signal-red: #e0262b;
    --paper: #ffffff;
  }
  * { box-sizing: border-box; margin: 0; padding: 0; }
  html, body { width: 960px; height: 1200px; overflow: hidden; }
  body {
    background: var(--stage);
    font-family: "Ubuntu", sans-serif;
    position: relative;
  }
  .card {
    position: absolute;
    top: 250px;
    width: 400px;
    height: 700px;
    border-radius: 20px;
    overflow: hidden;
    box-shadow: 0 10px 28px rgba(0,0,0,.18);
  }
  .card--front { left: 60px; background: var(--paper); }
  .card--back { left: 500px; background: var(--royal); }

  .card__art { position: absolute; inset: 0; width: 400px; height: 700px; }

  .brand {
    position: absolute;
    left: 0; right: 0;
    text-align: center;
    font-weight: 700;
    text-transform: uppercase;
    line-height: 1.05;
    font-size: 40px;
  }
  .brand__dot {
    display: block;
    width: 26px; height: 26px;
    border-radius: 50%;
    margin: 0 auto 14px;
  }
  .card--front .brand { top: 82px; color: var(--royal); }
  .card--front .brand__dot { background: var(--signal-red); }
  .card--back .brand { top: 210px; color: var(--paper); }
  .card--back .brand__dot { background: var(--paper); }

  .brand__est {
    position: absolute;
    left: 0; right: 0;
    text-align: center;
    font-size: 15px;
    letter-spacing: 3px;
    font-weight: 500;
  }
  .card--front .brand__est { top: 222px; color: var(--royal); }
  .card--back .brand__est { top: 350px; color: var(--paper); }

  .flourish {
    position: absolute;
    width: 70px; height: 20px;
    border-radius: 10px;
  }
  .card--front .flourish { left: 48px; top: 220px; background: rgba(43,76,155,.28); }
  .card--back .flourish { left: 165px; top: 430px; background: rgba(255,255,255,.3); }

  .contact {
    position: absolute;
    left: 58px;
    top: 392px;
    right: 40px;
    color: var(--paper);
  }
  .contact__name {
    color: var(--signal-red);
    font-size: 29px;
    font-weight: 500;
    text-transform: uppercase;
    letter-spacing: .5px;
  }
  .contact__title {
    font-size: 16px;
    text-transform: uppercase;
    letter-spacing: .5px;
    margin-top: 4px;
  }
  .contact__company {
    color: var(--signal-red);
    font-size: 19px;
    margin-top: 14px;
  }
  .contact__address { font-size: 17px; line-height: 1.35; margin-top: 2px; }
  .contact__lines { list-style: none; margin-top: 20px; }
  .contact__line {
    display: flex;
    align-items: center;
    gap: 10px;
    font-size: 19px;
    line-height: 1.55;
  }
  .contact__icon { width: 20px; height: 20px; flex: none; }

  .back__url {
    position: absolute;
    left: 0; right: 0;
    bottom: 92px;
    text-align: center;
    color: var(--paper);
    font-size: 15px;
    letter-spacing: 2.5px;
    text-transform: uppercase;
  }
</style>
</head>
<body>

<section class="card card--front" aria-label="Business card front">
  <svg class="card__art" viewBox="0 0 400 700" aria-hidden="true">
    <clipPath id="lower"><path d="M0,250 C80,225 120,300 190,335 C260,368 330,340 400,372 V700 H0 Z"/></clipPath>
    <path d="M0,250 C80,225 120,300 190,335 C260,368 330,340 400,372 V700 H0 Z" fill="var(--royal)"/>
    <path d="M40,18 H360 A22 22 0 0 0 382 40 V660 A22 22 0 0 0 360 682 H40 A22 22 0 0 0 18 660 V40 A22 22 0 0 0 40 18 Z"
          fill="none" stroke="var(--royal)" stroke-width="2"/>
    <path d="M40,18 H360 A22 22 0 0 0 382 40 V660 A22 22 0 0 0 360 682 H40 A22 22 0 0 0 18 660 V40 A22 22 0 0 0 40 18 Z"
          fill="none" stroke="var(--paper)" stroke-width="2" clip-path="url(#lower)"/>
  </svg>

  <div class="brand"><span class="brand__dot"></span>Kelbrook<br>Forge Co.</div>
  <div class="brand__est">EST. 1986</div>
  <div class="flourish" role="img" aria-label="Decorative scroll flourish"></div>

  <div class="contact">
    <p class="contact__name">Tom Pelling</p>
    <p class="contact__title">Sales &amp; Estimating</p>
    <p class="contact__company">Kelbrook Forge Co.</p>
    <p class="contact__address">48 Dunmore Ave Suite 3305<br>Alder Falls, OH 44074</p>
    <ul class="contact__lines">
      <li class="contact__line">
        <svg class="contact__icon" viewBox="0 0 20 20" aria-hidden="true"><circle cx="10" cy="10" r="10" fill="var(--signal-red)"/><path d="M6.5 5.5 L8.5 5.5 L9.3 8 L8 9 C8.7 10.5 9.5 11.3 11 12 L12 10.7 L14.5 11.5 L14.5 13.5 C10 14 6 10 6.5 5.5 Z" fill="var(--paper)"/></svg>
        (440) 555-0143
      </li>
      <li class="contact__line">
        <svg class="contact__icon" viewBox="0 0 20 20" aria-hidden="true"><circle cx="10" cy="10" r="10" fill="var(--signal-red)"/><rect x="5" y="6.5" width="10" height="7" fill="none" stroke="var(--paper)" stroke-width="1.4"/><path d="M5 6.5 L10 10.5 L15 6.5" fill="none" stroke="var(--paper)" stroke-width="1.4"/></svg>
        info@kelbrookforge.example
      </li>
      <li class="contact__line">
        <svg class="contact__icon" viewBox="0 0 20 20" aria-hidden="true"><circle cx="10" cy="10" r="10" fill="var(--signal-red)"/><circle cx="10" cy="10" r="5" fill="none" stroke="var(--paper)" stroke-width="1.3"/><path d="M5 10 H15 M10 5 C7.5 8 7.5 12 10 15 M10 5 C12.5 8 12.5 12 10 15" fill="none" stroke="var(--paper)" stroke-width="1.1"/></svg>
        www.kelbrookforge.example
      </li>
    </ul>
  </div>
</section>

<section class="card card--back" aria-label="Business card back">
  <svg class="card__art" viewBox="0 0 400 700" aria-hidden="true">
    <path d="M40,18 H360 A22 22 0 0 0 382 40 V660 A22 22 0 0 0 360 682 H40 A22 22 0 0 0 18 660 V40 A22 22 0 0 0 40 18 Z"
          fill="none" stroke="var(--paper)" stroke-width="2"/>
    <path d="M46,26 H354 A20 20 0 0 0 374 46 V654 A20 20 0 0 0 354 674 H46 A20 20 0 0 0 26 654 V46 A20 20 0 0 0 46 26 Z"
          fill="none" stroke="var(--paper)" stroke-width="1"/>
  </svg>

  <div class="brand"><span class="brand__dot"></span>Kelbrook<br>Forge Co.</div>
  <div class="brand__est">EST. 1986</div>
  <div class="flourish" role="img" aria-label="Decorative scroll flourish"></div>
  <p class="back__url">www.kelbrookforge.example</p>
</section>

</body>
</html>
```